Rapidly expanding Insulation business focusing on Sustainable and Energy Efficient Homes

Tidewell Home Insulation are specialist in;

- Insulation for Roof, Walls including existing/ closed cavity walls and underfloor.
- Domestic, new build and Commercial projects

We focus on Energy Efficiency by keeping your house warmer in winter and cooler in summer without having to have heating and air conditioning running all day and night.

Products used:

Fleecor- Pump in ceiling insulation, Combination of recycled paper mulch and wool with natural salts, borax and Boric acid to make it Fire and vermin proof. It has a lifetime warranty and is guaranteed "gap free" insulation unlike batt products.

Polyester batts- used for underfloor, walls and ceiling. A user friendly product that is also found in pillows, doonas and the like

Thermpak- Recycled polystyrene cube that is pumped down into existing wall cavities providing R-ratings of up to R6.0 (4.5 higher than the standard)

Fibreglass Batts- used for ceilings and wall. This is the cheapest product on the market

Acoustic Insulation- Generally used for commercial projects and also for new builds against rooms such as TV rooms, Bathrooms and entertaining areas.

Wall Wraps- For new builds

Our slogan
" your sustainable building solution"

Refer to our current websites that need modernising
www.tidewellhomeinsulation.com.au
www.thermpak.com.au

Target Market(s)

Domestic Home Owners, Domestic Builders and Commercial Builders

Industry/Entity Type

Insulation

Coding

Coded - Design and coding required

Number of Pages Required

5+ page

Font styles to use
Sans Serif

Requirements
Must have
• On top of the standard website format, I would like to have;
• blogging page
• Live chat
• Online enquiry
• Franchise/ Licensing enquiry page
• Gallery and videos
• Focus on key marketing words;
• Energy efficient
• Sustainable
Nice to have
• The general colours that we use are dark blue and red (like Tidewell logo)
Should not have
• Photos of other competitors installing materials

```html
<!DOCTYPE html>
<html lang="en">
<head>
<meta charset="utf-8">
<title>Tidewell Home Insulation</title>
<link href="https://fonts.googleapis.com/css2?family=Open+Sans:wght@400;600;700;800&family=Oswald:wght@400;500;600&display=swap" rel="stylesheet">
<style>
:root{
  --sun-1:#fbd66b;
  --sun-2:#f7a21c;
  --sun-3:#ee7a10;
  --orange:#f39a1e;
  --orange-dark:#e0780b;
  --blue:#1f5fa8;
  --blue-dark:#153f78;
  --blue-light:#2f86cf;
  --red:#d9262c;
  --text:#555b63;
  --muted:#8a9098;
  --line:#e3e6ea;
  --white:#ffffff;
}
*{box-sizing:border-box;margin:0;padding:0}
html,body{width:839px;height:1200px;overflow:hidden}
body{font-family:"Open Sans",Arial,sans-serif;color:var(--text);background:var(--white);position:relative;font-size:9px;line-height:1.45}
.sunburst{position:absolute;left:0;top:0;width:839px;height:520px;background:radial-gradient(ellipse at 20% 40%,#fff6cf 0%,var(--sun-1) 18%,var(--sun-2) 48%,var(--sun-3) 80%);}
.penguins{position:absolute;left:0;top:0;width:110px;height:350px;background:linear-gradient(180deg,#dfe8ee 0%,#9aa7b3 40%,#2e3640 75%,#e9eef2 100%);opacity:.85;border-radius:0 0 40px 0}
.brand{display:flex;align-items:center;gap:10px}
.site-brand{position:absolute;left:214px;top:18px}
.brand-mark{width:48px;height:48px;border-radius:50%;background:var(--blue);flex:none}
.brand-name{font-family:"Oswald",sans-serif;font-weight:500;font-size:24px;line-height:1.05;color:var(--white);text-transform:uppercase}
.live-chat{position:absolute;left:690px;top:24px;width:124px;height:56px;background:var(--red);border-radius:6px;color:var(--white);padding:10px 0 0 10px;font-weight:700}
.live-chat small{display:block;font-size:8px;font-weight:400}
.live-chat strong{font-size:13px;letter-spacing:.5px}
.agent{position:absolute;right:-6px;top:-8px;width:48px;height:48px;border-radius:50%;background:linear-gradient(#f4d7c2,#c88d6b);border:3px solid var(--white)}
.main-nav{position:absolute;left:182px;top:131px;width:574px;height:24px;background:linear-gradient(var(--blue-light),var(--blue));display:flex;justify-content:space-around;align-items:center;border-radius:2px}
.main-nav a{color:var(--white);text-decoration:none;font-weight:700;font-size:9px;letter-spacing:.4px}
.contact-panel{position:absolute;left:84px;top:306px;width:180px;background:var(--white);border-radius:4px;box-shadow:0 2px 6px rgba(0,0,0,.2)}
.contact-row{display:flex;gap:8px;align-items:center;padding:10px 10px;border-bottom:1px solid var(--line)}
.contact-row:last-child{border:0}
.icon-dot{width:22px;height:22px;border-radius:50%;background:var(--red);flex:none;display:flex;align-items:center;justify-content:center}
.contact-row span.label{display:block;font-size:8px;color:var(--muted)}
.contact-row b{color:var(--blue);font-size:13px}
.contact-row em{font-style:normal;font-size:7px;color:var(--blue)}
.hero{position:absolute;left:272px;top:172px;width:486px;height:334px;border:4px solid var(--white);box-shadow:0 2px 8px rgba(0,0,0,.25)}
.hero-photo{width:100%;height:100%;background:linear-gradient(160deg,#e6c35b 0%,#b8c27a 35%,#7ea04c 60%,#5f4a2a 100%)}
.tagline{position:absolute;left:-4px;bottom:-4px;right:-4px;height:40px;background:linear-gradient(90deg,var(--blue-dark),var(--blue-light));color:var(--white);font-family:"Oswald",sans-serif;font-size:15px;display:flex;align-items:center;padding-left:20px;gap:12px}
.tagline i{width:22px;height:22px;border-radius:50%;background:var(--orange);display:block}
.promo{position:absolute;left:70px;top:518px;width:714px;height:54px;background:var(--white);border-radius:4px;box-shadow:0 2px 6px rgba(0,0,0,.18);display:flex;align-items:center;padding:0 14px}
.promo h2{font-family:"Open Sans",sans-serif;font-weight:800;color:var(--orange-dark);font-size:19px}
.promo p{margin-left:8px;font-size:9px;color:var(--muted)}
.promo a{margin-left:auto;background:var(--orange);color:var(--white);padding:8px 16px;border-radius:3px;font-weight:700;text-decoration:none;font-size:9px}
.services{position:absolute;left:70px;top:594px;width:714px;display:flex;gap:10px}
.service{flex:1;height:106px;position:relative;background:linear-gradient(#e8c795,#b07a3e)}
.service:nth-child(2){background:linear-gradient(#d8d2c8,#8d7b66)}
.service:nth-child(3){background:linear-gradient(#f0c06a,#c8772a)}
.service:nth-child(4){background:linear-gradient(#e9cf8a,#a76b32)}
.service span{position:absolute;left:0;right:0;bottom:0;background:var(--orange);color:var(--white);font-weight:700;font-size:8px;padding:4px 6px}
.about{position:absolute;left:70px;top:714px;width:714px;display:flex;gap:16px}
.video{width:196px;height:126px;background:linear-gradient(#d7dde3,#8d979f);position:relative;flex:none}
.play{position:absolute;left:82px;top:47px;width:34px;height:32px;border-radius:8px;background:var(--red)}
.play:after{content:"";position:absolute;left:13px;top:9px;border-left:11px solid var(--white);border-top:7px solid transparent;border-bottom:7px solid transparent}
.about h1{font-family:"Oswald",sans-serif;font-weight:500;color:var(--blue);font-size:16px;margin:4px 0 8px}
.about p{margin-bottom:8px}
.row-lower{position:absolute;left:70px;top:862px;width:714px;display:flex;gap:16px}
.col-head{display:flex;justify-content:space-between;align-items:center;border-bottom:1px solid var(--line);padding-bottom:4px;margin-bottom:10px}
.col-head h3{font-family:"Oswald",sans-serif;font-weight:500;color:var(--blue);font-size:14px}
.arrows{display:flex;gap:3px}
.arrows i{width:10px;height:10px;background:var(--line);display:block}
.news{width:270px}
.news-item{display:flex;gap:8px}
.date{width:30px;height:36px;background:var(--red);color:var(--white);text-align:center;font-weight:700;font-size:12px;line-height:1;padding-top:5px;flex:none}
.date small{display:block;font-size:7px;font-weight:400}
.news-item b{color:var(--text);font-size:9px;display:block}
.news-item em{font-style:normal;color:var(--muted);font-size:7px}
.news p{margin-top:10px}
.gallery{flex:1}
.gallery-grid{display:flex;gap:8px}
.gallery-grid div{flex:1;height:78px;background:linear-gradient(#e85b2a,#f2c63b)}
.gallery-grid div:nth-child(2){background:linear-gradient(#d9d1c1,#8c806c)}
.gallery-grid div:nth-child(3){background:linear-gradient(#c9b89a,#7d6a4d)}
.footer{position:absolute;left:56px;top:1008px;width:744px;height:178px;background:var(--orange);color:var(--white);display:flex;padding:22px 22px;gap:28px}
.footer-brand{width:160px;flex:none}
.footer-brand .brand-mark{width:32px;height:32px}
.footer-brand .brand-name{font-size:15px}
.footer-brand small{display:block;margin-top:12px;font-size:7px}
.footer h4{font-size:10px;font-weight:700;margin-bottom:8px;text-transform:uppercase}
.footer ul{list-style:none;font-size:8px;line-height:1.9}
.footer-col{width:110px;flex:none}
.footer-contact{width:160px;flex:none;font-size:8px;line-height:1.9}
.social{display:flex;gap:5px;margin:6px 0 14px}
.social i{width:18px;height:18px;border-radius:50%;background:var(--white);opacity:.9;display:block}
.partner{width:120px;height:34px;background:var(--white);border-radius:4px}
</style>
</head>
<body>
<div class="sunburst"></div>
<div class="penguins" role="img" aria-label="Two emperor penguins standing in snow"></div>

<header>
  <div class="brand site-brand"><span class="brand-mark"></span><span class="brand-name">Tidewell<br>Home Insulation</span></div>
  <div class="live-chat"><small>Speak to us</small><strong>LIVE CHAT</strong><span class="agent" role="img" aria-label="Customer support agent portrait"></span></div>
  <nav class="main-nav"><a href="#">HOME</a><a href="#">ABOUT US</a><a href="#">BLOG</a><a href="#">ENQUIRY</a><a href="#">FRANCHISE</a><a href="#">CONTACT US</a></nav>
</header>

<aside class="contact-panel">
  <div class="contact-row"><span class="icon-dot"><svg width="11" height="11" viewBox="0 0 24 24"><path fill="#fff" d="M6.6 10.8a15 15 0 0 0 6.6 6.6l2.2-2.2c.3-.3.7-.4 1-.2 1.1.4 2.3.6 3.6.6.6 0 1 .4 1 1V20c0 .6-.4 1-1 1A17 17 0 0 1 3 4c0-.6.4-1 1-1h3.5c.6 0 1 .4 1 1 0 1.3.2 2.5.6 3.6.1.3 0 .7-.2 1z"/></svg></span><div><span class="label">Call us now :</span><b>1300 555 204</b></div></div>
  <div class="contact-row"><span class="icon-dot"><svg width="11" height="11" viewBox="0 0 24 24"><path fill="#fff" d="M2 5h20v14H2zm2 2v.5l8 5 8-5V7z"/></svg></span><div><span class="label">Email us now :</span><em>info@tidewellhomeinsulation.com.au</em></div></div>
</aside>

<section class="hero">
  <div class="hero-photo" role="img" aria-label="Tree in autumn and spring foliage across seasons"></div>
  <div class="tagline"><i></i>YOUR SUSTAINABLE, ENERGY EFFICIENT BUILDING SOLUTION</div>
</section>

<section class="promo">
  <h2>15% seniors card discount</h2>
  <p>(not to be used in conjunction with any other special offers)</p>
  <a href="#">CLICK HERE</a>
</section>

<section class="services">
  <div class="service" role="img" aria-label="Insulation batts in a roof space"><span>Insulation for Roofs</span></div>
  <div class="service" role="img" aria-label="Wall insulation being installed"><span>Walls including existing</span></div>
  <div class="service" role="img" aria-label="Closed cavity wall insulation"><span>Closed cavity walls</span></div>
  <div class="service" role="img" aria-label="Underfloor insulation"><span>Underfloor</span></div>
</section>

<section class="about">
  <div class="video" role="img" aria-label="Video of insulation being pumped into a ceiling"><span class="play"></span></div>
  <div>
    <h1>INSULATION SUPPLIES AND INSTALLATION</h1>
    <p>Insulating your home keeps it warmer in winter and cooler in summer, so heating and cooling no longer need to run all day and night. We supply and install energy efficient products for homes, new builds and commercial sites across the region.</p>
    <p>Choosing the right insulation for each roof, wall and floor lowers power bills and makes your home more sustainable. Our team will inspect your property, recommend the best product and complete the job quickly with minimal mess and a lifetime of comfort.</p>
  </div>
</section>

<section class="row-lower">
  <div class="news">
    <div class="col-head"><h3>LATEST NEWS</h3><span class="arrows"><i></i><i></i></span></div>
    <div class="news-item"><div class="date">28<small>March</small></div><div><b>Achieve the results need only one claim to do</b><em>by Tidewell · 3 Comments</em></div></div>
    <p>Energy efficient homes need the right insulation in every room. Read our latest tips on keeping your house comfortable all year round.</p>
  </div>
  <div class="gallery">
    <div class="col-head"><h3>GALLERY</h3><span class="arrows"><i></i><i></i></span></div>
    <div class="gallery-grid">
      <div role="img" aria-label="Thermal image of a house"></div>
      <div role="img" aria-label="Wall frame with insulation"></div>
      <div role="img" aria-label="Roof space with pumped insulation"></div>
    </div>
  </div>
</section>

<footer class="footer">
  <div class="footer-brand">
    <div class="brand"><span class="brand-mark"></span><span class="brand-name">Tidewell<br>Home Insulation</span></div>
    <small>© 2024 Tidewell Home Insulation<br>All rights reserved</small>
  </div>
  <div class="footer-col"><h4>Welcome</h4><ul><li>Home</li><li>About Us</li><li>Blog</li><li>Enquiry</li><li>Franchise</li><li>Contact Us</li></ul></div>
  <div class="footer-contact"><h4>Contact Info</h4>Tidewell Home Insulation<br>12 Harbour Lane<br>Portside VIC 3999<br>1300 555 204</div>
  <div><h4>Follow Us</h4><div class="social"><i></i><i></i><i></i><i></i></div><div class="partner" role="img" aria-label="Fleecor partner badge"></div></div>
</footer>
</body>
</html>
```